Restaurant DIGITAL menu design- menu items name and description typed in already

Menu design for vietnamese sandwich restaurant menu board. Design will be used in 6 feet tall by 4 feet wide format on four 4k tv mounted VERTICALLY. Main colours of design yellow, white, black. Design should be FUN AND CASUAL.

Target Market(s)

Young professionals in 30-40s age group

Requirements
Must have
• Please note that this is FOUR 4K tv mounted VERTICALLY. Two on top, two on bottom VERTICALLY. All horizontal design will NOT be considered as winner.

Please use menu information in "MAIN FILE" for design, no generic or incorrect information.

No stock photos, free or pay
Link for more images

https://www.filvarenstash.example/sh/kq3r8tzmpa2w47x/BBFR_7LNqTw4hxjj9uWMPZbc?dl=0
Should not have
• HORIZONTAL DESIGN WILL NOT BE CONSIDERED.
No Stock photos.

```html
<!DOCTYPE html>
<html lang="en">
<head>
<meta charset="utf-8">
<title>Fresh Juices Menu Board</title>
<link href="https://fonts.googleapis.com/css2?family=Montserrat:wght@500;600;700&display=swap" rel="stylesheet">
<style>
  :root {
    --stage: #2a2a2a;
    --board-yellow: #f6c244;
    --ink: #0b0b0b;
    --white: #ffffff;
    --photo-dark: #3a3530;
    --photo-warm: #c98a4a;
    --photo-green: #6f8d4a;
  }
  * { margin: 0; padding: 0; box-sizing: border-box; }
  html, body {
    width: 1200px; height: 675px; overflow: hidden;
    background: var(--stage);
    font-family: "Montserrat", sans-serif;
    color: var(--ink);
  }
  .menu-board {
    position: absolute;
    left: 425px; top: 27px;
    width: 350px; height: 620px;
    background: var(--board-yellow);
    overflow: hidden;
  }
  .section-pill {
    position: absolute;
    left: 36px; width: 277px; height: 41px;
    background: var(--ink);
    color: var(--white);
    border-radius: 21px;
    display: flex; align-items: center; justify-content: center;
    font-weight: 600; font-size: 30px; letter-spacing: 0.5px;
  }
  .pill-juices { top: 24px; }
  .pill-boost { top: 295px; }
  .menu-item { position: absolute; left: 0; width: 100%; }
  .item-tab {
    position: absolute; left: 0; top: 0;
    width: 22px; height: 30px;
    background: var(--ink);
  }
  .item-name {
    position: absolute; left: 30px; top: 0;
    font-weight: 700; font-size: 12.5px; line-height: 14px;
    white-space: nowrap;
  }
  .item-desc {
    position: absolute; left: 30px; top: 14px;
    font-weight: 500; font-size: 10.2px; line-height: 13px;
    white-space: nowrap;
  }
  .boost .item-name { font-size: 14.5px; line-height: 16px; top: 1px; }
  .boost .item-desc { font-size: 11.8px; top: 17px; }
  .photo-row {
    position: absolute; left: 0; top: 460px;
    width: 350px; height: 150px;
  }
</style>
</head>
<body>
  <main class="menu-board">
    <h1 class="section-pill pill-juices">FRESH JUICES</h1>

    <div class="menu-item" style="top:73px">
      <span class="item-tab"></span>
      <p class="item-name">GOOD MORNING: An A.M. Juice</p>
      <p class="item-desc">Apple | Pear | Carrot | Lemon | Orange 6</p>
    </div>
    <div class="menu-item" style="top:110px">
      <span class="item-tab"></span>
      <p class="item-name">GREEN GODDESS</p>
      <p class="item-desc">Celery | Cucumber | Green Apple | Pear | Lemon 6</p>
    </div>
    <div class="menu-item" style="top:147px">
      <span class="item-tab"></span>
      <p class="item-name">REVITALIZE</p>
      <p class="item-desc">Apple | Carrot | Lemon | Ginger 6</p>
    </div>
    <div class="menu-item" style="top:185px">
      <span class="item-tab"></span>
      <p class="item-name">POWER-UP</p>
      <p class="item-desc">Orange | Lemon | Ginger | Apple 6</p>
    </div>
    <div class="menu-item" style="top:223px">
      <span class="item-tab"></span>
      <p class="item-name">SOLA SIGNATURE</p>
      <p class="item-desc">Mango | Green Papaya | Pineapple | Lemon | Orange 6</p>
    </div>

    <h2 class="section-pill pill-boost">JUICE BOOST</h2>

    <div class="menu-item boost" style="top:357px">
      <span class="item-tab"></span>
      <p class="item-name">SUPERSEED BLEND (WITH COCONUT)</p>
      <p class="item-desc">A boost of ground flax, chia and hemp seed 0.75</p>
    </div>
    <div class="menu-item boost" style="top:407px">
      <span class="item-tab"></span>
      <p class="item-name">FLAXSEED WITH MIXED BERRIES</p>
      <p class="item-desc">A boost of ground flax, chia and hemp seed. 0.50</p>
    </div>

    <svg class="photo-row" viewBox="0 0 350 150" xmlns="http://www.w3.org/2000/svg">
      <defs>
        <radialGradient id="bowl-tone" cx="50%" cy="45%" r="60%">
          <stop offset="0%" stop-color="var(--photo-warm)"/>
          <stop offset="100%" stop-color="var(--photo-dark)"/>
        </radialGradient>
        <radialGradient id="sandwich-tone" cx="50%" cy="45%" r="60%">
          <stop offset="0%" stop-color="#d9a066"/>
          <stop offset="100%" stop-color="var(--photo-green)"/>
        </radialGradient>
        <radialGradient id="baguette-tone" cx="55%" cy="40%" r="60%">
          <stop offset="0%" stop-color="#e0b070"/>
          <stop offset="100%" stop-color="#2b2b2e"/>
        </radialGradient>
      </defs>
      <circle cx="184" cy="73" r="68" fill="url(#sandwich-tone)" stroke="var(--ink)" stroke-width="1" role="img" aria-label="Photo of a banh mi sandwich with pickled vegetables and cilantro"/>
      <circle cx="73" cy="73" r="68" fill="url(#bowl-tone)" stroke="var(--ink)" stroke-width="1" role="img" aria-label="Photo of a grilled chicken rice bowl with pickled carrots and a side of sauce"/>
      <circle cx="279" cy="73" r="68" fill="url(#baguette-tone)" stroke="var(--ink)" stroke-width="1" role="img" aria-label="Photo of a baguette sandwich with a cup of dipping sauce"/>
    </svg>
  </main>
</body>
</html>
```